Study Lantern

StudyLantern.com will be a place for people looking for information, resources, and advisement to start or continue their education. We want a friendly, inviting site design that makes finding what potential students are looking for simple and easy to navigate. We are not committed to the colors of the logo, so variations on the color scheme are welcome.

Text instructions based on the wireframe: For the site's homepage we'd like a banner at the very top for our Logo and white space to the right of it. See attachments for logo + wireframe. Below that would be navigation. Below that split into 2/3 on the left we would have home page content, and 1/3 on the right we would have the lead form. At the bottom of the page we would have a space for types of degrees, then a footer with copyright info + site info.

See wireframes for additional page layouts.

Industry/Entity Type

Education

Requirements
Must have
• At minimum we are looking for three pages: homepage, choose your degree path page, and content page.
Nice to have
• -White space is appreciated
-Variations on the color scheme are welcome, we are not married to the existing logo's color scheme.

```html
<!DOCTYPE html>
<html lang="en">
<head>
<meta charset="utf-8">
<title>Study Lantern</title>
<link href="https://fonts.googleapis.com/css2?family=Arimo:wght@400;700&display=swap" rel="stylesheet">
<style>
:root{
  --teal:#2b5f72;
  --teal-dark:#1f4c5c;
  --orange:#f26b1d;
  --text:#333;
  --muted:#666;
  --line:#cfd6da;
}
*{box-sizing:border-box;margin:0;padding:0}
html,body{width:866px;height:1200px;overflow:hidden;background:#fff}
body{position:relative;font-family:"Arimo",Arial,sans-serif;color:var(--text)}
.abs{position:absolute}

.brand{left:18px;top:28px;display:flex;align-items:center;gap:10px;font-size:38px;font-weight:700;color:var(--teal);letter-spacing:-.5px}
.brand-mark{width:22px;height:22px;border-radius:50%;background:var(--orange)}
.contact{left:703px;top:10px;font-size:12px;line-height:15.5px;color:#111}

.nav{left:16px;top:93px;width:838px;height:30px;border-radius:4px;background:linear-gradient(#35708a,var(--teal-dark));display:flex;align-items:center;padding-left:22px}
.nav a{color:#fff;text-decoration:none;font-size:12px;padding:5px 12px;margin-right:17px;border-radius:3px}
.nav a.active{background:var(--orange)}

.hero{left:16px;top:128px;width:838px;height:307px;background:var(--teal);border-radius:5px}
.hero-inner{left:8px;top:9px;width:822px;height:290px;background:#fff;border-radius:5px;overflow:hidden}
.hero-title{left:59px;top:78px;font-size:27px;line-height:51px;color:var(--teal-dark)}
.hero-photo{left:220px;top:0;width:560px;height:290px;background:radial-gradient(ellipse at 50% 60%,#d6a88c 0%,#9c6e5a 35%,#5f6f8a 62%,#fff 78%)}
.arrow{top:269px;width:24px;height:30px;background:var(--orange);border-radius:3px}
.hero-shadow{left:30px;top:436px;width:810px;height:14px;background:radial-gradient(ellipse at 50% 0,rgba(0,0,0,.18),transparent 70%)}

.h2{font-size:15px;color:#111;text-transform:uppercase}
.h2 .teal{color:var(--teal);font-size:16px}
.h2 .accent{color:var(--orange);font-size:16px}
.welcome{left:49px;top:479px}
.welcome-rule{left:49px;top:497px;width:252px;border-top:1px dotted #777}
.intro{left:50px;top:516px;width:510px;font-size:12px;line-height:18px}
.intro p{margin-bottom:18px}
.intro .lead{color:var(--teal);margin-bottom:17px}

.how-title{left:49px;top:705px}
.steps{left:34px;top:737px;width:537px;height:158px;border-radius:4px;background:radial-gradient(ellipse at 50% 40%,#fff 40%,#ececec 100%)}
.step{position:absolute;display:flex;align-items:center;gap:10px;font-size:12px;line-height:16px}
.step svg{flex:none}

.types-title{left:49px;top:931px}
.type{width:220px}
.type h3{font-size:13px;font-weight:400;margin-bottom:10px}
.type p{font-size:9.5px;line-height:16px;color:#333}
.more{display:flex;align-items:center;gap:9px;font-size:10px;margin-top:14px;color:#333}
.more i{width:10px;height:10px;border-radius:50%;background:#222;display:inline-block}

.form{left:620px;top:470px;width:225px;height:476px;border:1px solid var(--line);border-radius:6px;box-shadow:0 1px 4px rgba(0,0,0,.12)}
.ribbon{left:611px;top:482px;width:233px;height:38px;background:var(--teal);color:var(--orange);font-size:16px;padding:10px 0 0 22px}
.ribbon-fold{left:611px;top:520px}
.form-intro{left:631px;top:530px;width:205px;font-size:9.5px;line-height:16px}
.form-cta{left:631px;top:576px;font-size:12px;color:var(--orange)}
.field{position:absolute;left:628px;width:207px;height:20px;display:flex;align-items:center;justify-content:space-between;font-size:9px}
.field b{color:#c00;font-weight:400}
.input{width:116px;height:20px;border:1px solid #cfd6da;border-radius:4px;background:linear-gradient(#fff,#eef1f3);position:relative}
.select::after{content:"";position:absolute;right:7px;top:6px;width:5px;height:5px;border-right:2px solid var(--teal);border-bottom:2px solid var(--teal);transform:rotate(45deg)}
.triple{display:flex;gap:3px}
.triple .input{width:37px}
.submit{left:660px;top:893px;width:160px;height:37px;border-radius:19px;background:linear-gradient(#ffa050,var(--orange));border:2px solid #e05a10;box-shadow:0 0 0 2px #fbd3b5;display:flex;align-items:center;justify-content:center;gap:6px;font-size:12px;font-weight:700;color:#222}
.privacy{left:635px;top:961px;width:200px;font-size:9.5px;line-height:16px}

.footer{left:16px;top:1091px;width:838px;height:64px;border-radius:4px;background:linear-gradient(#35708a,var(--teal-dark))}
.social{left:30px;top:20px;display:flex;gap:4px}
.social i{width:18px;height:18px;border-radius:3px;background:#4a90c8;display:block}
.social i:last-child{background:var(--orange)}
.foot-links{right:30px;top:14px;font-size:10px;color:#fff}
.foot-links span{margin:0 9px;color:#cfe}
.copy{right:33px;top:40px;font-size:9.5px;color:#fff}
</style>
</head>
<body>

<div class="abs brand"><span class="brand-mark"></span>Study Lantern</div>
<div class="abs contact">Contact :<br>48 Orchard Lane<br>Fairhaven, CA 95012<br>Telephone: 555-014-2200<br>Facsimile: 555-014-2201</div>

<nav class="abs nav">
  <a class="active">About Us</a><a>Degrees</a><a>How it Works</a><a>Contact Us</a><a>Privacy Policy</a><a>Terms of Us</a><a>Feed back</a>
</nav>

<section class="abs hero">
  <div class="abs hero-inner">
    <div class="abs hero-photo" role="img" aria-label="Group of smiling students holding books and folders"></div>
    <div class="abs hero-title">Invest In Your<br>Future Today!</div>
  </div>
</section>
<svg class="abs arrow" style="left:16px" viewBox="0 0 24 30"><path d="M9 9l6 6-6 6" stroke="#fff" stroke-width="3" fill="none"/></svg>
<svg class="abs arrow" style="left:830px" viewBox="0 0 24 30"><path d="M15 9l-6 6 6 6" stroke="#fff" stroke-width="3" fill="none"/></svg>
<div class="abs hero-shadow"></div>

<h2 class="abs h2 welcome">Welcome to <span class="teal">Study</span> <span class="accent">Lantern</span></h2>
<div class="abs welcome-rule"></div>
<div class="abs intro">
  <p class="lead">Invest In Your Future Today!</p>
  <p>Are you overwhelmed by the thought of choosing the right college?</p>
  <p>StudyLantern helps simplify this process by matching colleges to you and your needs. Tell us about yourself and let us do the work for you.</p>
  <p>Take control of your future by furthering your education.</p>
</div>

<h2 class="abs h2 how-title">How it <span class="accent">Works</span></h2>
<div class="abs steps">
  <div class="step" style="left:32px;top:16px">
    <svg width="36" height="36" viewBox="0 0 36 36"><rect x="4" y="2" width="26" height="32" fill="#fff" stroke="#222" stroke-width="2"/><path d="M9 10h16M9 16h16M9 22h12" stroke="#666" stroke-width="2"/></svg>
    <span>Tell us about yourself.<br>Complete the form.</span>
  </div>
  <div class="step" style="left:284px;top:16px">
    <svg width="42" height="30" viewBox="0 0 42 30"><path d="M2 10L21 3l19 7-19 7z" fill="#222"/><path d="M10 14v8c0 3 22 3 22 0v-8l-11 4z" fill="#333"/><path d="M36 12v10" stroke="#c9a227" stroke-width="2"/></svg>
    <span>Get matched.<br>Request info from schools.</span>
  </div>
  <div class="step" style="left:24px;top:84px">
    <svg width="44" height="40" viewBox="0 0 44 40"><circle cx="22" cy="12" r="9" fill="#3a2a22"/><path d="M6 40c0-12 8-18 16-18s16 6 16 18z" fill="#c8102e"/></svg>
    <span>Talk to enrollment advisors.</span>
  </div>
  <div class="step" style="left:296px;top:96px">
    <svg width="26" height="30" viewBox="0 0 26 30"><rect x="1" y="3" width="24" height="26" rx="2" fill="#eee" stroke="#555"/><rect x="1" y="3" width="24" height="7" fill="#c8102e"/><text x="13" y="25" font-size="11" text-anchor="middle" font-family="Arimo,sans-serif" fill="#222">15</text></svg>
    <span>Enroll in your school</span>
  </div>
</div>

<h2 class="abs h2 types-title">Degree <span class="accent">Types</span></h2>
<article class="abs type" style="left:53px;top:966px">
  <h3>Nunc varius facilisis eros</h3>
  <p>Nunc varius facilisis eros. Sed erat. In in velitquis arcu ornare laoreet. luctus massa.Nunc varius facilisis eros. Sed erat.</p>
  <div class="more"><i></i>MORE</div>
</article>
<article class="abs type" style="left:340px;top:966px">
  <h3>Nunc varius facilisis eros</h3>
  <p>Nunc varius facilisis eros. Sed erat. In in velitquis arcu ornare laoreet. luctus massa.Nunc varius facilisis eros. Sed erat.</p>
  <div class="more"><i></i>MORE</div>
</article>

<aside>
  <div class="abs form"></div>
  <div class="abs ribbon">Tell us more about YOU!</div>
  <svg class="abs ribbon-fold" width="9" height="8" viewBox="0 0 9 8"><path d="M0 0h9v8z" fill="#173c49"/></svg>
  <p class="abs form-intro">StudyLantern provides you with accredited school information that match your interests.</p>
  <p class="abs form-cta">Get matched to the right schools today.</p>

  <div class="field" style="top:600px"><span>Subject<b>*</b></span><div class="input select"></div></div>
  <div class="field" style="top:631px"><span>Degree Level<b>*</b></span><div class="input select"></div></div>
  <div class="field" style="top:662px"><span>High School Grad Yr.<b>*</b></span><div class="input select"></div></div>
  <div class="field" style="top:693px"><span>First Name<b>*</b></span><div class="input"></div></div>
  <div class="field" style="top:725px"><span>Last Name<b>*</b></span><div class="input"></div></div>
  <div class="field" style="top:756px"><span>Street Address<b>*</b></span><div class="input"></div></div>
  <div class="field" style="top:787px"><span>Zip / City / State<b>*</b></span><div class="triple"><div class="input select"></div><div class="input select"></div><div class="input select"></div></div></div>
  <div class="field" style="top:818px"><span>Phone Number<b>*</b></span><div class="input"></div></div>
  <div class="field" style="top:849px"><span>Email Address<b>*</b></span><div class="input"></div></div>

  <div class="abs submit">
    <svg width="14" height="18" viewBox="0 0 14 18"><path d="M3 8V5a4 4 0 018 0v3" stroke="#555" stroke-width="2" fill="none"/><rect x="1" y="8" width="12" height="10" rx="1" fill="#b8860b"/></svg>
    Request Information
  </div>
  <p class="abs privacy">Your information will be kept strictly private as stated in our Privacy Policy.</p>
</aside>

<footer class="abs footer">
  <div class="abs social"><i></i><i></i><i></i><i></i></div>
  <div class="abs foot-links">About Us<span>|</span>Degrees<span>|</span>How it Works<span>|</span>Contact Us<span>|</span>Privacy Policy<span>|</span>Terms of Us<span>|</span>Feed back</div>
  <div class="abs copy">© 2012 Study Lantern. All Rights Reserved</div>
</footer>

</body>
</html>
```